Falcon Letterhead

Looking for a design template for our company’s official letterheads & business cards.It has to be mainly white and include our company logo, website, social media handle, address, phone number. Visit our website to have an idea of our brand identity and colours. Please use the same font that we are using in our website.
Target Market(s)
Lubricants & Greases, Industrial markets, Automotive
Font styles to use
Other font styles liked:
- Saira Extra-Condensed
Colors
ffffff
000000
fbee3f
Requirements
Must have
- It must be consistent with our brand identity. It must use the same exact yellow (Pantone color: 102C) and black (Pantone color: K100) as our brand colors.
- Must also use our font attached (Saira.zip). It's called Saira Extra-Condensed.
- We intend to use the FALCON logo and not the small mini-FN logo.
- On the design we must include ALL of the following:
- E-mail: info@falconoils.example
- @FalconGreases
- www.falconoils.example
- Address: P.O. Boc 4728, Qurain 53004, Kuwait
- Phone: (+965) 24718395
- Gulf Marwa Oils logo (attached). The logo attached is in Blue/Red but you can select one solid color for all of it such as BLACK or YELLOW depending on what background color you'll select.
Nice to have
- Like it to be as professional and as modern as possible. It has look clean, slick and classy.
Should not have
- Too many different colors.

```html
<!DOCTYPE html>
<html lang="en">
<head>
<meta charset="utf-8">
<title>Falcon Letterhead</title>
<link rel="stylesheet" href="https://fonts.googleapis.com/css2?family=Saira+Extra+Condensed:wght@500;700&family=Montserrat:wght@500&display=swap">
<style>
  :root {
    --brand-yellow: #fbee3f;
    --brand-black: #000000;
    --paper: #ffffff;
    --backdrop: #cbcbcb;
    --partner-blue: #1d4fa8;
    --watermark: #f4f4f4;
    --ink-soft: #1a1a1a;
  }
  html, body {
    margin: 0;
    padding: 0;
    width: 1200px;
    height: 1200px;
    overflow: hidden;
    background: var(--backdrop);
  }
  .canvas {
    position: relative;
    width: 1200px;
    height: 1200px;
  }
  .letterhead {
    position: absolute;
    left: 211px;
    top: 50px;
    width: 778px;
    height: 1100px;
    background: var(--paper);
    overflow: hidden;
    font-family: "Saira Extra Condensed", sans-serif;
    color: var(--brand-black);
  }
  .contact {
    position: absolute;
    right: 52px;
    top: 40px;
    display: flex;
    align-items: stretch;
    gap: 12px;
    font-weight: 500;
    font-size: 16px;
    line-height: 1.3;
    color: var(--ink-soft);
    white-space: nowrap;
  }
  .contact-block.left { text-align: right; }
  .contact-divider {
    width: 2px;
    background: var(--brand-yellow);
  }
  .brand {
    position: absolute;
    left: 52px;
    top: 118px;
    white-space: nowrap;
  }
  .brand-badge {
    display: inline-flex;
    align-items: center;
    background: var(--brand-yellow);
    border-radius: 0 0 22px 22px;
    padding: 4px 22px 2px 18px;
  }
  .brand-name {
    font-weight: 700;
    font-size: 60px;
    line-height: 1;
    letter-spacing: 1px;
  }
  .brand-handle {
    display: block;
    text-align: right;
    font-weight: 700;
    font-size: 17px;
    margin-top: 4px;
    padding-right: 12px;
  }
  .watermark {
    position: absolute;
    left: 0;
    right: 0;
    top: 470px;
    text-align: center;
    font-weight: 700;
    font-size: 140px;
    line-height: 1;
    color: var(--watermark);
    white-space: nowrap;
    user-select: none;
  }
  .partner {
    position: absolute;
    right: 60px;
    bottom: 110px;
    display: flex;
    align-items: center;
    gap: 14px;
    white-space: nowrap;
  }
  .partner-dot {
    width: 56px;
    height: 56px;
    border-radius: 50%;
    background: var(--partner-blue);
  }
  .partner-name {
    font-family: "Montserrat", sans-serif;
    font-weight: 500;
    font-size: 24px;
    color: var(--partner-blue);
    letter-spacing: 0.5px;
  }
  .footer-band {
    position: absolute;
    left: 0;
    bottom: 0;
    width: 100%;
    height: 14px;
    display: flex;
  }
  .band-yellow { background: var(--brand-yellow); }
  .band-black { background: var(--brand-black); }
</style>
</head>
<body>
  <div class="canvas">
    <main class="letterhead">
      <header>
        <div class="contact">
          <div class="contact-block left">
            <div>(+965) 24718395</div>
            <div>P.O. Boc 4728, Qurain 53004, Kuwait</div>
          </div>
          <div class="contact-divider"></div>
          <div class="contact-block right">
            <div>www.falconoils.example</div>
            <div>info@falconoils.example</div>
          </div>
        </div>
        <div class="brand">
          <div class="brand-badge">
            <span class="brand-name">FALCON</span>
          </div>
          <span class="brand-handle">@FalconGreases</span>
        </div>
      </header>

      <div class="watermark" aria-hidden="true">FALCON</div>

      <footer>
        <div class="partner">
          <div class="partner-dot"></div>
          <span class="partner-name">GULF MARWA OILS CO.</span>
        </div>
        <div class="footer-band">
          <div class="band-yellow" style="width:24%"></div>
          <div class="band-black" style="width:24%"></div>
          <div class="band-yellow" style="width:22%"></div>
          <div class="band-black" style="width:30%"></div>
        </div>
      </footer>
    </main>
  </div>
</body>
</html>
```